New homepage design www.marblequill.nl

We need a new website design to go with our new designed logo.
We are a relativly small basketballclub that would like a shiny new webdesign for our homepage. We want te be able to create a real homepage/base for our clubmembers, where they can find news, upcoming events (agenda/calendar) and the related info on playing basketball at our club (games/tasks/teams and all).

The current website is located at: www.marblequill.nl but is an outdated and not so appealing design.
There are no real designfeatures of the current site that have to be transferred to the new site.
Coding in HTML/CSS/JS/JPEG/PNG is enough, making a dynamic website will be my task. I just need the design in HTML (preferrably HTML 5)

There is not a huge budget, we are a club without a main sponsor.

Feel free to be creative and amaze us!

Text for the page in the new design will be created by us, you may use some sample text for filling.

Currently used pictures in the site don't have to be transferred to the new page (preferrably not!)

Reason: For Newyear/holiday reasons

Tomorrow we will pick a design.

• The new logo as uploaded and attached.
News page.
Agenda page
HTML compatible same look and feel in all modern browsers (IE, FireFox, Chrome, Safari)
• HTML 5 validated and approved

```html
<!DOCTYPE html>
<html lang="en">
<head>
<meta charset="utf-8">
<title>BC Marblequill – Home</title>
<link href="https://fonts.googleapis.com/css2?family=Bebas+Neue&family=Oswald:wght@400;500;700&family=Open+Sans:wght@400;700&display=swap" rel="stylesheet">
<style>
:root{
  --navy:#21364f;
  --orange:#f08a2b;
  --grey:#77777a;
  --grey-text:#6f6f71;
  --white:#ffffff;
  --footer-text:#555555;
  --thumb-border:#cfcfcf;
}
*{box-sizing:border-box;margin:0;padding:0}
html,body{width:1200px;height:1046px;overflow:hidden;background:var(--white)}
body{position:relative;font-family:"Open Sans",sans-serif}
.hero{position:absolute;left:0;top:0;width:1200px;height:464px;background:linear-gradient(#f3f3f3,#d9d9d9)}
.brand{position:absolute;left:150px;top:78px;display:flex;align-items:center;gap:8px;font-family:"Oswald",sans-serif;font-weight:700;font-size:26px;color:var(--navy)}
.brand-dot{width:22px;height:22px;border-radius:50%;background:var(--orange)}
.main-nav{position:absolute;left:324px;top:20px;width:747px;height:46px;background:var(--navy);border-bottom:4px solid #8a8a8a;display:flex;overflow:hidden}
.main-nav a{font-family:"Bebas Neue",sans-serif;font-size:24px;color:var(--white);text-decoration:none;padding:0 14.5px;line-height:44px;white-space:nowrap}
.main-nav a.active{background:var(--grey);padding:0 19px 0 22px;margin-right:0}
.welcome{position:absolute;left:155px;top:204px;font-family:"Oswald",sans-serif;font-weight:700;font-size:60px;color:var(--navy);letter-spacing:-1px}
.welcome-sub{position:absolute;left:157px;top:285px;width:310px;font-family:"Oswald",sans-serif;font-weight:500;font-size:38px;line-height:44px;color:var(--grey-text);letter-spacing:-1px}
.welcome-sub em{font-style:normal;color:var(--orange)}
.hero-photo{position:absolute;left:500px;top:80px;width:530px;height:384px;background:radial-gradient(ellipse at 50% 55%,#c98a4d 0%,#9a8e86 45%,rgba(217,217,217,0) 72%)}
.info-band{position:absolute;left:0;top:464px;width:1200px;height:134px;background:var(--navy);padding:21px 117px 0}
.info-band p{color:#e4e8ee;font-size:14px;line-height:17px;width:945px}
.announce{position:absolute;left:118px;top:619px;width:452px;height:319px;background:var(--orange);padding:16px 13px;color:var(--white)}
.announce h2{font-family:"Oswald",sans-serif;font-weight:500;font-size:25px;line-height:34px;margin-bottom:12px}
.announce p{font-size:12px;line-height:14.6px;width:412px}
.announce ul{margin:10px 0 0 0;list-style:none}
.announce li{font-size:12px;line-height:14.5px;position:relative;padding-left:14px}
.announce li::before{content:"";position:absolute;left:0;top:5px;width:5px;height:5px;border-radius:50%;background:var(--white)}
.read-more{position:absolute;left:13px;top:274px;font-family:"Oswald",sans-serif;font-weight:500;font-size:19px;color:var(--white);text-decoration:none}
.read-more small{font-size:11px}
.teams{position:absolute;left:580px;top:619px;width:500px;height:173px;background:var(--grey);padding:8px 18px}
.teams h2{font-family:"Oswald",sans-serif;font-weight:500;font-size:25px;color:var(--white);line-height:34px;margin-bottom:2px}
.team-cols{display:flex;gap:42px}
.team-cols ul{list-style:none;width:208px}
.team-cols li{font-size:12px;color:#f2f2f2;line-height:21px;border-bottom:1px solid #d8d8d8;margin-bottom:1px}
.gallery-head{position:absolute;left:583px;top:800px;width:497px;display:flex;justify-content:space-between;align-items:flex-end;font-family:"Oswald",sans-serif}
.gallery-head h2{font-weight:500;font-size:31px;color:var(--grey-text);line-height:40px}
.gallery-head a{font-weight:400;font-size:19px;color:var(--grey-text);text-decoration:none;margin-bottom:2px}
.thumb{position:absolute;top:843px;height:95px;border:3px solid var(--thumb-border);background:linear-gradient(#8b8f96,#3f63a8 55%,#b9a27a)}
.thumb.hall{background:linear-gradient(#9a9c94,#8c8a7e 50%,#b79a78)}
.footer-line{position:absolute;left:0;top:964px;width:1200px;height:2px;background:#d4d4d4}
.footer-nav{position:absolute;left:118px;top:985px;display:flex;gap:13px}
.footer-nav a{font-family:Arial,sans-serif;font-size:12.5px;color:var(--footer-text);text-decoration:none}
.copyright{position:absolute;left:118px;top:1004px;font-family:Arial,sans-serif;font-size:11px;color:#888}
.social{position:absolute;left:808px;top:989px;display:flex;gap:9px}
.social span{width:28px;height:28px;border-radius:50%;background:#9d9d9d}
.footer-brand{position:absolute;left:1008px;top:994px;font-family:"Oswald",sans-serif;font-weight:700;font-size:14px;color:#8d8d8d}
</style>
</head>
<body>
<header class="hero">
  <div class="brand"><span class="brand-dot"></span>MARBLEQUILL</div>
  <nav class="main-nav">
    <a class="active" href="#">HOME</a><a href="#">TEAMS</a><a href="#">INFORMATION</a><a href="#">GALLERY</a><a href="#">CONTACT</a><a href="#">LINKS</a><a href="#">GUESTBOOK</a><a href="#">LOGIN</a>
  </nav>
  <h1 class="welcome">WELKOM</h1>
  <p class="welcome-sub">Het bestuur van BC <em>Marblequill</em> heet je welkom op onze site.</p>
  <div class="hero-photo" role="img" aria-label="Two young basketball players, a young man and a young woman, posing with basketballs"></div>
</header>

<section class="info-band">
  <p><strong>CLOTHING:</strong> If you do not yet have complete basketball clothes, think of Kindled Hoops. Marblequill is going to work. These sports in Elmvoort together This sporting goods store has all the necessary stuff for basketball. Think of shoes, a dress or suits. The choice is well represented, and there is also a nice discount on! So if you need new stuff, then just walk in Kindled Hoops in Elmvoort inside. Indicate that you are a member of Marblequill and the discount will be deducted. Of all purchases from members of Marblequill association gets as a small amount. This will be invested in new materials. Thus, our association members both helped!</p>
</section>

<section class="announce">
  <h2>IMPORTANT ANNOUNCEMENTS:</h2>
  <p>IMPORTANT DATES: throughout the season, there are a few dates that we are unfortunately not able to make use of the sports hall or gymnasium Oakmere Hall use. Ther are also a number of important other data. Consider the transition from the Tuesday of the sports hall to hall Oakmere Hall (and back again). Below is a summary of these important dates:</p>
  <ul>
    <li>31-12-2013 No training related New Year's Eve</li>
    <li>20-02-2014 No training related carnival</li>
    <li>24-02-2014 No training related carnival</li>
    <li>25-02-2014 No training related carnival</li>
    <li>27-02-2014 No training related carnival</li>
    <li>03-03-2014 No training related carnival</li>
    <li>04-03-2014 No training related carnival</li>
  </ul>
  <a class="read-more" href="#">READ MORE <small>+</small></a>
</section>

<section class="teams">
  <h2>TEAMS</h2>
  <div class="team-cols">
    <ul><li>01. Ladies Recreaten 1</li><li>02. Seneor Women 1</li><li>03. Externals</li><li>04. Recereaten Men</li><li>05. Seneor Men 1</li></ul>
    <ul><li>Ladies Recreaten 1</li><li>Seneor Women 1</li><li>Externals</li><li>Recereaten Men</li><li>Seneor Men 1</li></ul>
  </div>
</section>

<div class="gallery-head"><h2>GALLERY</h2><a href="#">MORE</a></div>
<div class="thumb" style="left:584px;width:143px" role="img" aria-label="Team photo of players in blue kits in a sports hall"></div>
<div class="thumb hall" style="left:737px;width:128px" role="img" aria-label="Players resting on the floor of a sports hall"></div>
<div class="thumb" style="left:875px;width:96px" role="img" aria-label="Team photo of players in blue kits"></div>
<div class="thumb hall" style="left:982px;width:99px" role="img" aria-label="Players sitting in a sports hall"></div>

<div class="footer-line"></div>
<footer>
  <nav class="footer-nav">
    <a href="#">HOME</a><a href="#">TEAMS</a><a href="#">INFORMATION</a><a href="#">GALLERY</a><a href="#">CONTACT</a><a href="#">LINKS</a><a href="#">GUESTBOOK</a><a href="#">LOGIN</a>
  </nav>
  <p class="copyright">© Copyright 2002 - 2013 Company Name. All Rights Reserved</p>
  <div class="social"><span aria-label="Social link"></span><span aria-label="Social link"></span><span aria-label="Social link"></span></div>
  <div class="footer-brand">MARBLEQUILL</div>
</footer>
</body>
</html>
```